Holvern Incorporated

Holvern is a business that provides consulting, and manages and supplies trades persons in the construction and heavy industries sector. We build, do maintenance, install machinery, and can manage projects or jobs. Would like or prefer more clean, classic designs. Blacks/greys, but open to almost anything.

Target Market(s)

Industrial/Construction/Manufacturing

Industry/Entity Type

Construction Company

Contact Information for Business Card

Clean, business name on the front, possibly have the details on the back, but open to any ideas.

Logo Text

We currently do not have a slogan, open to ideas

Font styles to use
Serif
Sans Serif

Colors

Designer to choose colors to be used in the design.

Requirements
Should not have
• the oval is not my logo, was just an idea. please don't send 20 designs with the oval

```html
<!DOCTYPE html>
<html lang="en">
<head>
<meta charset="utf-8">
<title>Holvern Incorporated – Business Card</title>
<link href="https://fonts.googleapis.com/css2?family=Bitter:wght@500&family=Fira+Sans:wght@400;500&display=swap" rel="stylesheet">
<style>
  :root {
    --canvas: #9a9b9e;
    --card-black: #0b0b0c;
    --card-white: #efefef;
    --ink: #111111;
    --ink-soft: #3a3a3a;
    --paper-ink: #f4f4f4;
    --pattern-light: #1c1c1e;
  }
  * { margin: 0; padding: 0; box-sizing: border-box; }
  html, body {
    width: 1200px;
    height: 675px;
    overflow: hidden;
    background: var(--canvas);
  }
  .stage {
    position: relative;
    width: 1200px;
    height: 675px;
    display: flex;
    align-items: center;
    justify-content: center;
    gap: 60px;
  }
  .card {
    position: relative;
    width: 490px;
    height: 280px;
    overflow: hidden;
    box-shadow: 0 10px 24px rgba(0,0,0,0.25);
  }

  /* Front */
  .card-front {
    background: var(--card-black);
    display: flex;
    flex-direction: column;
    align-items: center;
    justify-content: center;
  }
  .front-pattern {
    position: absolute;
    inset: 0;
    background: linear-gradient(135deg, var(--card-black) 0%, var(--pattern-light) 50%, var(--card-black) 100%);
  }
  .wordmark {
    position: relative;
    font-family: "Bitter", Georgia, serif;
    font-weight: 500;
    font-size: 58px;
    line-height: 1;
    letter-spacing: 1px;
    color: var(--paper-ink);
  }
  .wordmark-sub {
    position: relative;
    margin-top: 8px;
    font-family: "Bitter", Georgia, serif;
    font-weight: 500;
    font-size: 10px;
    letter-spacing: 3px;
    color: var(--paper-ink);
  }

  /* Back */
  .card-back {
    background: var(--card-white);
    color: var(--ink);
    font-family: "Fira Sans", Arial, sans-serif;
  }
  .phone {
    position: absolute;
    top: 26px;
    left: 30px;
    font-size: 20px;
    letter-spacing: 0.5px;
  }
  .details {
    position: absolute;
    top: 74px;
    right: 30px;
    text-align: right;
  }
  .person-name {
    font-size: 24px;
    font-weight: 500;
    line-height: 1.1;
  }
  .person-role {
    font-size: 11px;
    color: var(--ink-soft);
    margin-top: 4px;
  }
  .divider {
    display: inline-block;
    width: 12px;
    height: 1.5px;
    background: var(--ink);
    margin: 8px 0 6px;
  }
  .contact-line {
    font-size: 15px;
    line-height: 1.35;
  }
  .back-brand {
    position: absolute;
    left: 30px;
    bottom: 24px;
  }
  .back-brand .wordmark {
    color: var(--ink);
    font-size: 46px;
  }
  .back-brand .wordmark-sub {
    color: var(--ink);
    font-size: 8px;
    margin-top: 4px;
    text-align: right;
  }
</style>
</head>
<body>
  <main class="stage">
    <section class="card card-front" aria-label="Card front">
      <div class="front-pattern" role="img" aria-label="Decorative pattern of diagonal white strokes on black"></div>
      <div class="wordmark">Holvern</div>
      <div class="wordmark-sub">INCORPORATED</div>
    </section>

    <section class="card card-back" aria-label="Card back">
      <div class="phone">+041-5550172</div>
      <div class="details">
        <div class="person-name">Dorian Kessler</div>
        <div class="person-role">Owner</div>
        <span class="divider"></span>
        <div class="contact-line">dorian@holvern.com</div>
        <div class="contact-line">Holvern.com</div>
        <div class="contact-line">14 Ridgeway Street, California</div>
      </div>
      <div class="back-brand">
        <div class="wordmark">Holvern</div>
        <div class="wordmark-sub">INCORPORATED</div>
      </div>
    </section>
  </main>
</body>
</html>
```